Brackmoor Gin Label

Anfield is an area of Liverpool. We have no desire for those who are aware of the area to associate it with football. We have a copy of Holcrest Gin which is our brand attached to the files. Please can you read this and replicate but in red. Thanks.

```html
<!DOCTYPE html>
<html lang="en">
<head>
<meta charset="utf-8">
<title>Brackmoor Gin Label</title>
<link href="https://fonts.googleapis.com/css2?family=Alfa+Slab+One&family=Barlow+Semi+Condensed:wght@400;500;700&family=Great+Vibes&family=Oswald:wght@500&family=Playfair+Display:wght@700&display=swap" rel="stylesheet">
<style>
  :root {
    --paper: #dfe6df;
    --red: #a31c22;
    --red-deep: #931a1f;
    --gold: #c9a040;
    --ink: #3a3a3a;
    --page: #ffffff;
  }
  html, body { margin: 0; padding: 0; overflow: hidden; }
  body { width: 1200px; height: 2468px; background: var(--page); position: relative; }
  .label, .neck-tag { position: absolute; display: block; }
  .label { left: 0; top: 0; width: 760px; height: 740px; }
  .neck-tag { left: 910px; top: 260px; width: 150px; height: 310px; }
  .serif-caps { font-family: "Playfair Display", serif; font-weight: 700; letter-spacing: 6px; }
  .slab { font-family: "Alfa Slab One", serif; }
  .sans { font-family: "Barlow Semi Condensed", sans-serif; }
  .script { font-family: "Great Vibes", cursive; }
  .numeral { font-family: "Oswald", sans-serif; font-weight: 500; }
</style>
</head>
<body>

<svg class="label" viewBox="0 0 760 740" xmlns="http://www.w3.org/2000/svg">
  <defs>
    <path id="distillery-arc" d="M205,112 Q380,82 555,112"/>
    <path id="brand-arc" d="M130,280 Q400,130 672,280"/>
  </defs>

  <!-- label body with scalloped top and bottom edges, straight sides -->
  <path class="label-body" fill="var(--paper)" d="
    M42,22
    q8,-8 16,0 q8,8 16,0 q8,-8 16,0 q8,8 16,0 q8,-8 16,0 q8,8 16,0 q8,-8 16,0 q8,8 16,0
    q8,-8 16,0 q8,8 16,0 q8,-8 16,0 q8,8 16,0 q8,-8 16,0 q8,8 16,0 q8,-8 16,0 q8,8 16,0
    q8,-8 16,0 q8,8 16,0 q8,-8 16,0 q8,8 16,0 q8,-8 16,0 q8,8 16,0 q8,-8 16,0 q8,8 16,0
    q8,-8 16,0 q8,8 16,0 q8,-8 16,0 q8,8 16,0 q8,-8 16,0 q8,8 16,0 q8,-8 16,0 q8,8 16,0
    q8,-8 16,0 q8,8 16,0 q8,-8 16,0 q8,8 16,0 q8,-8 16,0 q8,8 16,0 q8,-8 16,0 q8,8 16,0
    q8,-8 16,0 q8,8 16,0 q8,-8 16,0
    L730,714
    q-8,8 -16,0 q-8,-8 -16,0 q-8,8 -16,0 q-8,-8 -16,0 q-8,8 -16,0 q-8,-8 -16,0 q-8,8 -16,0 q-8,-8 -16,0
    q-8,8 -16,0 q-8,-8 -16,0 q-8,8 -16,0 q-8,-8 -16,0 q-8,8 -16,0 q-8,-8 -16,0 q-8,8 -16,0 q-8,-8 -16,0
    q-8,8 -16,0 q-8,-8 -16,0 q-8,8 -16,0 q-8,-8 -16,0 q-8,8 -16,0 q-8,-8 -16,0 q-8,8 -16,0 q-8,-8 -16,0
    q-8,8 -16,0 q-8,-8 -16,0 q-8,8 -16,0 q-8,-8 -16,0 q-8,8 -16,0 q-8,-8 -16,0 q-8,8 -16,0 q-8,-8 -16,0
    q-8,8 -16,0 q-8,-8 -16,0 q-8,8 -16,0 q-8,-8 -16,0 q-8,8 -16,0 q-8,-8 -16,0 q-8,8 -16,0 q-8,-8 -16,0
    q-8,8 -16,0 q-8,-8 -16,0 q-8,8 -16,0
    L42,22 Z"/>

  <!-- illustration area -->
  <rect class="illustration" role="img" aria-label="Engraved illustration of a distiller in a top hat standing beside a barrel" x="80" y="458" width="118" height="212" rx="6" fill="#d6b9b4" opacity="0.6"/>

  <!-- distillery arc -->
  <text class="serif-caps distillery" font-size="17" fill="var(--red)" text-anchor="middle">
    <textPath href="#distillery-arc" startOffset="50%">KESTREL DISTILLERY</textPath>
  </text>

  <!-- brand name -->
  <text class="slab brand-name" font-size="92" fill="var(--red)" text-anchor="middle">
    <textPath href="#brand-arc" startOffset="50%" textLength="530" lengthAdjust="spacingAndGlyphs">BRACKMOOR</textPath>
  </text>
  <text class="slab brand-gin" x="385" y="445" font-size="210" fill="var(--red)" text-anchor="middle" textLength="320" lengthAdjust="spacingAndGlyphs">GIN</text>

  <!-- info lines -->
  <text class="sans botanicals" x="384" y="500" font-size="21" font-weight="500" fill="var(--red)" text-anchor="middle" letter-spacing="1">8 FINE BOTANICALS</text>
  <text class="sans region" x="388" y="532" font-size="30" font-weight="700" fill="var(--gold)" text-anchor="middle" transform="rotate(-2 388 532)">MERSYSIDE, ENGLAND</text>
  <text class="sans method" x="384" y="570" font-size="21" font-weight="500" fill="var(--red)" text-anchor="middle" letter-spacing="1">HAND DISTILLET</text>

  <!-- dashed rules -->
  <line x1="170" y1="587" x2="680" y2="587" stroke="var(--ink)" stroke-width="1" stroke-dasharray="3 3"/>
  <line x1="170" y1="626" x2="680" y2="626" stroke="var(--ink)" stroke-width="1" stroke-dasharray="3 3"/>

  <text class="script small-batch" x="238" y="618" font-size="44" fill="var(--red)">Small batch Gin</text>

  <!-- spec row -->
  <text class="sans spec-label" x="230" y="641" font-size="10" fill="var(--ink)">DISTILLER</text>
  <text class="script signature" x="206" y="662" font-size="28" fill="var(--red)">Signature</text>
  <line x1="310" y1="630" x2="310" y2="660" stroke="var(--ink)" stroke-width="1"/>
  <text class="sans spec-label" x="315" y="641" font-size="10" fill="var(--ink)">ALCOHOL</text>
  <text class="numeral spec-value" x="370" y="656" font-size="24" fill="var(--ink)">40%VOL</text>
  <line x1="466" y1="630" x2="466" y2="660" stroke="var(--ink)" stroke-width="1"/>
  <text class="sans spec-label" x="470" y="641" font-size="10" fill="var(--ink)">VOLUMEN</text>
  <text class="numeral spec-value" x="520" y="656" font-size="24" fill="var(--ink)">70 CL</text>

  <!-- maker mark -->
  <g class="maker-mark">
    <circle cx="620" cy="558" r="22" fill="none" stroke="var(--gold)" stroke-width="2"/>
    <text class="sans maker-name" x="620" y="612" font-size="17" font-weight="500" fill="var(--gold)" text-anchor="middle">Fenwright Gin Co.</text>
  </g>
</svg>

<svg class="neck-tag" viewBox="0 0 150 310" xmlns="http://www.w3.org/2000/svg">
  <path class="tag-body" fill="var(--red-deep)" d="M9,7 H140 V282 Q132,282 132,299 H17 Q17,282 9,282 Z"/>
  <circle cx="75" cy="130" r="24" fill="none" stroke="var(--gold)" stroke-width="2"/>
  <text class="sans maker-name" x="75" y="180" font-size="14" font-weight="500" fill="var(--gold)" text-anchor="middle">Fenwright Gin Co.</text>
  <text class="sans tag-title" x="75" y="253" font-size="20" font-weight="700" fill="var(--gold)" text-anchor="middle">BRACKMOOR</text>
  <text class="sans tag-title" x="75" y="271" font-size="20" font-weight="700" fill="var(--gold)" text-anchor="middle">LONDON</text>
  <text class="sans tag-title" x="75" y="289" font-size="20" font-weight="700" fill="var(--gold)" text-anchor="middle">DRY GIN</text>
</svg>

</body>
</html>
```